HiItsJonBrell.com needs a modern, eye-catching business card design

My name is Jon Brell and I own a video training (software development industry) website. I need a business card design that is eye catching for when I travel to conferences or do seminars. I would prefer something simple but bold. Something along the lines of this: https://pixvaultstatic.example/gallery_img/530172/44018/44018_9917302_530172_image.jpg

Note that I do not have a specific logo, but I do have an caricature I use on my site of myself. I've not attached it because I'm not really a fan of having it on my business cards. I would prefer lettering instead of an image. You can go to my website (https://hiitsjonbrell.com) for inspiration.

I want to add the following information on my card (the order of these, their size, and their casing is up to you):

Jon Brell
jon@HiItsJonBrell.com
@HiItsJonBrell
HiItsJonBrell.com
vidsharehub.example/HiItsJonBrell

I would also like to have somewhere on the card a small ad that says "Get a free course at https://HiItsJonBrell.com/FreeCourse". Feel free to play with that wording or layout if you need. I would prefer this text to be at the bottom of the card and subtle. Some small eye-catching thing might be ok but nothing huge or garish.

I plan on printing this card at pressquill.example (https://www.pressquill.example/us/design-guidelines/business-cards.html). I would like it to be the standard size (3.66" x 2.16"). I would prefer rounded corners and horizontal orientation. This is a two-side design. I would prefer the side with all of the information be primarily white but I like color text (again, flexible on that). On the front side, I like simple. Maybe just HiItsJonBrell.com (casing on that is up to you - whatever looks and reads the best - that goes for all of the casing). As for font choices, I prefer a modern, clean font. For example, Open Sans Light can be a nice option.

Website Info (might be helpful for the card):
Color Palette

Darkest blue - #263246
Alternate blue - #2F4E6A
Light blue - #2A98C3
Orange - #FF6201
White - #FFFFFF

Font for Jon Brell Logo

Jellyka Estryas Handwriting
http://www.typecrate.example/jellyka_estryas_handwriting.font

Fonts for Site Content and VidShare Thumbnails

Lovelo (bold title font)
http://www.glyphmill.example/lovelo-font/

Open Sans (body font)
http://www.letterbarn.example/fonts/open-sans

Industry/Entity Type

Software Development

Contact Information for Business Card

Jon Brell
jon@HiItsJonBrell.com
@HiItsJonBrell
HiItsJonBrell.com
vidsharehub.example/HiItsJonBrell

Get a free course at https://HiItsJonBrell.com/FreeCourse

Colors

Designer to choose colors to be used in the design.

Requirements
Nice to have
• Modern color - maybe primarily a color on the front and then that color as an accent on the back.
Should not have
• Lots of colors - I LOVE color but do not want a rainbow of colors on the card.

```html
<!DOCTYPE html>
<html lang="en">
<head>
<meta charset="utf-8">
<title>Jon Brell – Business Card</title>
<link rel="stylesheet" href="https://fonts.googleapis.com/css2?family=Open+Sans:wght@300;400;600&display=swap">
<style>
  :root {
    --darkest-blue: #263246;
    --alt-blue: #2F4E6A;
    --light-blue: #2A98C3;
    --orange: #FF6201;
    --white: #FFFFFF;
    --stage: #ECEDEF;
    --divider: #B9BDC4;
  }
  * { box-sizing: border-box; margin: 0; padding: 0; }
  html, body {
    width: 1200px; height: 900px; overflow: hidden;
    background: var(--stage);
    font-family: "Open Sans", Arial, sans-serif;
  }
  .canvas {
    width: 1200px; height: 900px;
    display: flex; flex-direction: column;
    align-items: center; justify-content: center; gap: 30px;
  }
  .card {
    width: 700px; height: 413px;
    border-radius: 22px;
    position: relative;
    box-shadow: 0 8px 24px rgba(38, 50, 70, 0.18);
    overflow: hidden;
  }
  .card-front {
    background: linear-gradient(160deg, var(--alt-blue) 0%, var(--darkest-blue) 70%);
    display: flex; align-items: center; justify-content: center;
  }
  .front-domain {
    color: var(--white);
    font-weight: 400;
    font-size: 44px;
    letter-spacing: 0.5px;
  }
  .card-back {
    background: linear-gradient(180deg, var(--white) 0%, #F1F2F4 100%);
  }
  .brand-name {
    position: absolute;
    left: 70px; top: 160px;
    font-size: 56px;
    font-weight: 300;
    color: var(--darkest-blue);
    letter-spacing: 0.5px;
  }
  .divider {
    position: absolute;
    left: 365px; top: 120px;
    width: 2px; height: 150px;
    background: var(--divider);
  }
  .contact-list {
    position: absolute;
    left: 385px; top: 124px;
    list-style: none;
    display: flex; flex-direction: column; gap: 12px;
  }
  .contact-item {
    display: flex; align-items: center; gap: 10px;
    font-size: 15px;
    color: var(--darkest-blue);
    white-space: nowrap;
  }
  .contact-icon {
    width: 22px; height: 22px; flex: none;
    border-radius: 50%;
    display: flex; align-items: center; justify-content: center;
  }
  .icon-social { background: var(--light-blue); }
  .icon-mail, .icon-web { background: var(--darkest-blue); }
  .icon-video { background: var(--orange); }
  .course-band {
    position: absolute;
    left: 170px; right: 30px; bottom: 42px;
    height: 36px;
    border-radius: 10px;
    background: var(--darkest-blue);
    color: var(--white);
    font-size: 16px;
    display: flex; align-items: center; justify-content: center;
    letter-spacing: 0.3px;
  }
</style>
</head>
<body>
<main class="canvas">
  <section class="card card-front">
    <p class="front-domain">HiItsJonBrell.com</p>
  </section>

  <section class="card card-back">
    <h1 class="brand-name">Jon Brell</h1>
    <div class="divider"></div>
    <ul class="contact-list">
      <li class="contact-item"><span class="contact-icon icon-social"></span>@HiItsJonBrell</li>
      <li class="contact-item">
        <span class="contact-icon icon-mail">
          <svg width="12" height="9" viewBox="0 0 12 9"><rect x="0.5" y="0.5" width="11" height="8" rx="1" fill="none" stroke="#FFFFFF" stroke-width="1"/><path d="M0.8 1 L6 5 L11.2 1" fill="none" stroke="#FFFFFF" stroke-width="1"/></svg>
        </span>jon@HiItsJonBrell.com</li>
      <li class="contact-item">
        <span class="contact-icon icon-web">
          <svg width="13" height="13" viewBox="0 0 13 13"><circle cx="6.5" cy="6.5" r="5.5" fill="none" stroke="#FFFFFF" stroke-width="1"/><ellipse cx="6.5" cy="6.5" rx="2.4" ry="5.5" fill="none" stroke="#FFFFFF" stroke-width="1"/><line x1="1" y1="6.5" x2="12" y2="6.5" stroke="#FFFFFF" stroke-width="1"/></svg>
        </span>www.HiItsJonBrell.com</li>
      <li class="contact-item"><span class="contact-icon icon-video"></span>vidsharehub.example/HiItsJonBrell</li>
    </ul>
    <p class="course-band">Get a free course at : https://HiItsJonBrell.com/FreeCourse</p>
  </section>
</main>
</body>
</html>
```